Brightbay Business Card Design

Our company is called Brightbay. We manufacture confectionary snacks & frozen novelties. Our initial product portfolio includes frozen ice lollies/popsicles & stick ice cream bars.

We require a business card design.

Please use the attached Logo.

Please use an orange, brown, yellow colour code. You may choose any combination of the 3 or include all three. The logo however must remain orange.

Target Market(s)

Business card will be targeted at distributors of our products such as supermarket procurement managers, convenience store owners, wholesale distributors and merchandising agents.

Industry/Entity Type

Business

Requirements
Must have
• Calvin Obeng_Director/ P.O.Box Dunmore 5172, Accra, Ghana / m: 00233(0)507318924/ e: calvin.obeng@mailvora.co.uk

```html
<!DOCTYPE html>
<html lang="en">
<head>
<meta charset="utf-8">
<title>Brightbay Business Card</title>
<link rel="stylesheet" href="https://fonts.googleapis.com/css2?family=Pathway+Gothic+One&display=swap">
<style>
  :root {
    --page-bg: #ffffff;
    --card-bg: #ded3d3;
    --brand-orange: #f07022;
    --ink: #1e1a1a;
    --decor-tone: rgba(196, 188, 188, 0.7);
    --ground-shadow: rgba(90, 84, 84, 0.45);
  }
  * { margin: 0; padding: 0; box-sizing: border-box; }
  html, body {
    width: 1200px;
    height: 900px;
    overflow: hidden;
    background: var(--page-bg);
  }
  .card {
    position: absolute;
    left: 72px;
    top: 132px;
    width: 1056px;
    height: 636px;
    background: var(--card-bg);
    overflow: hidden;
    font-family: "Pathway Gothic One", "Arial Narrow", sans-serif;
    color: var(--ink);
  }
  .card__backdrop {
    position: absolute;
    left: 38px;
    top: 10px;
    width: 640px;
    height: 640px;
    border-radius: 44% 44% 30% 30%;
    background: radial-gradient(ellipse at 45% 50%, var(--decor-tone) 0%, rgba(196,188,188,0.3) 55%, rgba(222,211,211,0) 78%);
  }
  .brand {
    position: absolute;
    left: 62px;
    top: 282px;
    display: flex;
    align-items: center;
    gap: 24px;
  }
  .brand__dot {
    width: 84px;
    height: 84px;
    border-radius: 50%;
    background: var(--brand-orange);
  }
  .brand__name {
    font-size: 162px;
    line-height: 1;
    color: var(--brand-orange);
    font-weight: 400;
  }
  .brand-ground {
    position: absolute;
    left: 30px;
    top: 468px;
    width: 620px;
    height: 12px;
    border-radius: 50%;
    background: radial-gradient(ellipse at 50% 50%, var(--ground-shadow) 0%, rgba(90,84,84,0) 70%);
  }
  .contact {
    position: absolute;
    right: 46px;
    top: 316px;
    text-align: right;
  }
  .contact__name {
    font-size: 58px;
    line-height: 1;
    margin-bottom: 8px;
  }
  .contact__line {
    font-size: 31px;
    line-height: 44px;
  }
</style>
</head>
<body>
  <div class="card">
    <div class="card__backdrop" role="img" aria-label="Soft grey background artwork area behind the brand name"></div>

    <div class="brand">
      <span class="brand__dot"></span>
      <span class="brand__name">Brightbay</span>
    </div>
    <div class="brand-ground"></div>

    <div class="contact">
      <p class="contact__name">Calvin Obeng</p>
      <p class="contact__line">Director</p>
      <p class="contact__line">P.O.Box Dunmore 5172,</p>
      <p class="contact__line">Accra, Ghana</p>
      <p class="contact__line">m: 00 233 (0) 507 318 924</p>
      <p class="contact__line">e: calvin.obeng@mailvora.co.uk</p>
    </div>
  </div>
</body>
</html>
```